Velmarcoteni Business cards

Dear team, I need to get the design file to suit it to our team. The focus of the business card is the Automotive Market and the design must be in black colour and the logo must be in glossy black. On the front of the card I need to get the following info:

- Name and Surname
- Title
- eMail
- Phone Number
- Skype account
- domain address

```html
<!DOCTYPE html>
<html lang="es">
<head>
<meta charset="utf-8">
<title>Velmarcoteni – Business cards</title>
<link href="https://fonts.googleapis.com/css2?family=Montserrat:wght@400;500;700;800&display=swap" rel="stylesheet">
<style>
  :root {
    --bg: #d9d9db;
    --card: #2b2b2d;
    --card-back-a: #3a3a3c;
    --card-back-b: #161617;
    --red: #e3222b;
    --white: #ffffff;
    --light: #e6e6e6;
  }
  * { margin: 0; padding: 0; box-sizing: border-box; }
  html, body {
    width: 1200px; height: 1186px; overflow: hidden;
    background: var(--bg);
    font-family: "Montserrat", sans-serif;
  }
  .card {
    position: absolute; left: 170px;
    width: 860px; height: 491px;
    border-radius: 28px;
    box-shadow: 0 14px 30px rgba(0,0,0,.25);
    overflow: hidden;
  }
  .card-back { top: 70px; }
  .back-pattern {
    width: 100%; height: 100%;
    background: linear-gradient(135deg, var(--card-back-a) 0%, var(--card-back-b) 70%);
  }
  .card-front { top: 625px; background: var(--card); }
  .brand {
    position: absolute; left: 70px; top: 212px;
    display: flex; align-items: center; gap: 16px;
  }
  .brand-square { width: 54px; height: 54px; background: var(--red); }
  .brand-name {
    color: var(--white); font-weight: 700; font-size: 50px; letter-spacing: -0.5px;
  }
  .divider {
    position: absolute; left: 488px; top: 115px;
    width: 2px; height: 260px; background: var(--red);
  }
  .contact { position: absolute; left: 520px; top: 112px; color: var(--light); }
  .person-name {
    color: var(--red); font-weight: 800; font-size: 27px; letter-spacing: .5px;
    text-transform: uppercase; line-height: 1.1;
  }
  .person-title { font-size: 19px; color: var(--white); margin-bottom: 16px; }
  .contact-list { list-style: none; font-size: 18px; }
  .contact-list li { display: flex; align-items: center; gap: 12px; height: 31px; }
  .contact-icon { width: 17px; height: 17px; flex: none; }
  .address { font-size: 18px; line-height: 1.35; margin-top: 14px; }
</style>
</head>
<body>
  <section class="card card-back">
    <div class="back-pattern" role="img" aria-label="Glossy black repeating pattern of the brand mark with one red accent tile"></div>
  </section>

  <section class="card card-front">
    <div class="brand">
      <span class="brand-square"></span>
      <span class="brand-name">Velmarcoteni</span>
    </div>

    <div class="divider"></div>

    <div class="contact">
      <div class="person-name">Mateo Rivas</div>
      <div class="person-title">Comercial</div>
      <ul class="contact-list">
        <li>
          <svg class="contact-icon" viewBox="0 0 24 24"><path fill="#e3222b" d="M6.6 10.8a15 15 0 0 0 6.6 6.6l2.2-2.2a1 1 0 0 1 1-.25 11.4 11.4 0 0 0 3.6.57 1 1 0 0 1 1 1V20a1 1 0 0 1-1 1A17 17 0 0 1 3 4a1 1 0 0 1 1-1h3.5a1 1 0 0 1 1 1c0 1.25.2 2.45.57 3.57a1 1 0 0 1-.25 1z"/></svg>
          600 12 34 56
        </li>
        <li>
          <svg class="contact-icon" viewBox="0 0 24 24"><rect x="2" y="5" width="20" height="14" rx="2" fill="#e3222b"/><path d="M3 6l9 7 9-7" fill="none" stroke="#2b2b2d" stroke-width="2"/></svg>
          redazione@velmarcoteni.com
        </li>
        <li>
          <svg class="contact-icon" viewBox="0 0 24 24"><circle cx="12" cy="12" r="10" fill="#e3222b"/></svg>
          @velmarcoteni
        </li>
        <li>
          <svg class="contact-icon" viewBox="0 0 24 24"><circle cx="12" cy="12" r="10" fill="#e3222b"/><path d="M2 12h20M12 2c3 3 3 17 0 20M12 2c-3 3-3 17 0 20" fill="none" stroke="#2b2b2d" stroke-width="1.6"/></svg>
          www.velmarcoteni.com
        </li>
      </ul>
      <div class="address">Pol. Ind. Norte, C/4 nº 12<br>41870 Valdeluna</div>
    </div>
  </section>
</body>
</html>
```